Web Design for Solar Energy Consultancy Company

~ May 3, 2017 Update ~
As our project is rapidly progressing towards its completion, we started building up the list of designs that attracted the most of the team's attention. Additional submittals are still most welcome. Before submitting your proposal, however, we can recommend to review the concepts that received 4 stars as these are the ones that, in our opinion, most closely match the brief's requirements. Thank you!!
~ April 30, 2017 Update ~
The project deadline has been extended to attract a broader design community and to better tailor the final design to the requirements of the project.
A "light", "clean" (minimalistic), professionally looking, unique design is expected. Please, try to avoid industry cliches. Also, please use green, which became another industry cliche, with great caution. The brief provides minimum details to foster creativity. With the same notion in mind, the page content information is not provided.
Thank you for your feedback and support of the project!!
~ April 22, 2017 Update ~
Additional comments after starting receiving more designs:
- your attention to the brief's requirements will be highly appreciated. It is expected that the design is unique - standard, commonly used, images, formats and approaches do not fall under this category. There is no need to "bombard" with slightly different variations of the same design. It is expected that a conceptual (preliminary) design is submitted first, and, after it is reviewed (each design will receive a star rating and, if the star rating is greater than 3, a detailed feedback), the requested changes are implemented. We believe this will allow to approach the design process more efficiently and safe additional time to both the Designers's Community and our company. Thank you for understanding.
Clarification, please submit two variations of a design:
1) 1 page "business card" design that the company will be able to use during its startup stage;
2) the fully functional design (as per the requirements outlined below) for the company to transition to after the start-up period is over. Same design principles as developed for option 1 should be used for this variation.
Additional clarification, please note that the news block will not require images (at least during the start-up stage). It is envisioned to be a news feeder.
~ April 21, 2017 Update ~
Preliminary comments after receiving first designs:
- please try to create a unique design, using common elements wisely. Though such solar energy "attributes" as a solar panel or a bulb are very well recognized and allow quickly identify the nature of the business, they also became so common that in many cases a design may seem very similar to the one of others (Oh!, I've already seen this... effect).
- please try to introduce the company's logo unobtrusively. The size and position of the logo should clearly identify the company, but the message should be subtle, the logo should not distract from the main design. Brask's swoosh did not need to occupy have the screen.
- please use the green color with caution as it was with the company's logo. True, it is a green energy. But there is no need for the color to "scream" about it. Use the amount of green and its tone (avoid acid green) wisely.
--------------------------------------------------------------------------------
1. Main Goal
Develop a website that can represent the company to the industry stakeholders and become its "business card" during the start-up stage.
2. Secondary Goal
Develop a structure of a fully functional website that the "business card" design can eventually be transformed to staying consistent with the original design principles.
3. Key Audience
Varolu Corp. is providing consulting and technical services in the area of Solar Energy. The industry stakeholders include project developers, financial community, governmental bodies, OEMs, and competition.
4. Site Map
- HOME
• About
• Services
• Solar Energy
• News
• Contacts
• Social Media
- SERVICES*
- PROJECTS*
- FINANCE*
- TRAINING*
- SOLAR (ENERGY)*
* Maybe inactive / partially functional during the start-up stage.
5. Technical Specifications
Online brochure website during the start-up stage with a capability to be eventually transformed to a fully functional website while preserving the original design principles.
The design to be appealing, "light", professional, and with an intuitive and easy to navigate interface. Modern coding principles supporting efficiency and security to be utilized. Newest industry trends in website coding will be welcome.
The website to be designed so that it would fit well a computer, tablet, or mobile phone screen of any size. Cross-platform functionality to be taken into consideration to ensure that the website is fully functional on any platform.
Company's logo has already been designed and will be shared with the short-listed designers during the final design stage.
6. Interaction
The website will provide information about the company, our services, and projects. In addition, the industry insight, accumulated knowledge, and most recent trends are planned to be shared with stakeholders and attract and retain the audience.
Interaction with designers during the website development is envisioned to go through the following steps:
a) conceptual design - to be proposed by a designer originally. All conceptual designs will be reviewed and a feedback provided to pre-selected designers;
b) (preliminary and) final design - depending on the level of additional changes required can be broken into two steps. After discussing preliminary designs, company images will be provided to the selected finalists, who will compete with their final proposals.
7. Industry Stakeholders
- https://www.quellbrin.com/power/solar-power.- http://www.pakortavon.com/
- http://www.vellitrazo.com/about/company/
- https://www.oruxem.com/energy/index.html
8. Budget
Defined by the project.
9. Timescale
Defined by the project.
12. Additional Info
- No copy-cats, standard graphics, or cliches please!
- Additional information / clarifications will be gladly provided upon request.
- This specification may be updated throughout the project to reflect discussions with / changes proposed by the Designers community.

```html
<!DOCTYPE html>
<html lang="en">
<head>
<meta charset="utf-8">
<title>Varolu Corp – Solar Power Consultancy</title>
<link href="https://fonts.googleapis.com/css2?family=Roboto:wght@300;400;500;700&display=swap" rel="stylesheet">
<style>
:root{
  --green:#1f9d55;
  --green-band:#2fa866;
  --orange:#f39c12;
  --ink:#222222;
  --body:#555555;
  --muted:#888888;
  --grey-bg:#f3f3f3;
  --footer:#262626;
  --footer-deep:#1c1c1c;
  --footer-text:#bdbdbd;
  --white:#ffffff;
}
*{box-sizing:border-box;margin:0;padding:0}
html,body{width:1200px;height:3249px;overflow:hidden}
body{font-family:"Roboto",Arial,sans-serif;color:var(--body);background:var(--white);position:relative}
.abs{position:absolute}
p{font-size:12.5px;line-height:22px}
.more{color:var(--orange)}

/* header */
.site-header{position:absolute;left:0;top:0;width:1200px;height:80px;background:var(--white)}
.brand{position:absolute;left:88px;top:24px;display:flex;align-items:center;gap:10px;font-size:24px;font-weight:500;color:var(--ink)}
.brand-dot{width:26px;height:26px;border-radius:50%;background:var(--orange)}
.main-nav{position:absolute;left:505px;top:30px;display:flex;gap:28px;font-size:14px;color:var(--ink);align-items:center}
.btn-contact{position:absolute;left:1008px;top:20px;width:102px;height:38px;background:var(--green);color:var(--white);font-size:13px;font-weight:500;display:flex;align-items:center;justify-content:center}

/* hero */
.hero{position:absolute;left:0;top:80px;width:1200px;height:480px;background:linear-gradient(180deg,#3d4e6a 0%,#8a6a5c 45%,#d98a45 70%,#2b2620 100%)}
.hero-title{position:absolute;top:175px;width:100%;text-align:center;font-size:56px;font-weight:400;color:var(--white)}
.hero-sub{position:absolute;top:244px;width:100%;text-align:center;font-size:28px;font-weight:300;color:var(--white)}
.btn-start{position:absolute;left:536px;top:292px;width:128px;height:36px;background:var(--white);color:var(--ink);font-size:13px;display:flex;align-items:center;justify-content:center}
.hero-arrow{position:absolute;top:282px;width:28px;height:44px;background:rgba(255,255,255,.35)}

/* sections */
.section-title{position:absolute;width:100%;text-align:center;font-size:32px;font-weight:400;color:var(--ink)}
.photo{position:absolute}
.sub-title{font-size:19px;color:var(--ink);font-weight:400;margin-bottom:10px}

/* services */
.services{position:absolute;left:0;top:1142px;width:1200px;height:476px;background:linear-gradient(90deg,#29a060,#3cb372)}
.service-item{position:absolute;left:702px;display:flex;gap:24px;align-items:center;color:var(--white)}
.service-icon{width:56px;height:56px;border-radius:50%;background:var(--white);display:flex;align-items:center;justify-content:center}
.service-icon.active{background:var(--orange)}
.service-item h4{font-size:15px;font-weight:500;margin-bottom:4px}
.service-item p{font-size:12.5px;line-height:18px}

/* projects */
.filters{position:absolute;left:620px;top:1672px;display:flex;gap:18px;font-size:12px;color:var(--ink);text-transform:uppercase}
.filters .on{color:var(--orange);border-bottom:2px solid var(--orange);padding:0 4px 4px}

/* news */
.news{position:absolute;left:0;top:2192px;width:1200px;height:570px;background:var(--grey-bg)}
.date{position:absolute;width:46px;height:50px;color:var(--white);font-size:13px;font-weight:700;text-align:center;line-height:18px;padding-top:7px}
.news-title{position:absolute;font-size:17px;color:var(--ink)}
.byline{position:absolute;font-size:12px;color:var(--muted)}

/* footer */
.site-footer{position:absolute;left:0;top:2762px;width:1200px;height:487px;background:var(--footer);color:var(--footer-text)}
.f-brand{color:var(--white)}
.contact-circle{position:absolute;width:50px;height:50px;border-radius:50%;background:#333;display:flex;align-items:center;justify-content:center}
.f-col{position:absolute;top:148px}
.f-col h5{font-size:15px;font-weight:500;color:var(--white);margin-bottom:16px}
.f-col li{list-style:none;font-size:12.5px;line-height:28.5px}
.social li{display:flex;align-items:center;gap:10px;line-height:36px}
.social .dot{width:24px;height:24px;border-radius:50%;background:#444}
.copyright{position:absolute;left:0;top:438px;width:1200px;height:49px;background:var(--footer-deep);font-size:12px;text-align:center;line-height:49px}
.to-top{position:absolute;left:1142px;top:3176px;width:36px;height:36px;border-radius:50%;background:var(--white);display:flex;align-items:center;justify-content:center}
</style>
</head>
<body>

<header class="site-header">
  <div class="brand"><span class="brand-dot"></span>Varolu Corp.</div>
  <nav class="main-nav">
    <svg width="14" height="14" viewBox="0 0 14 14"><path d="M1 7 7 1l6 6h-2v6H3V7z" fill="#1f9d55"/></svg>
    <span>About Us</span><span>Services</span><span>Projects</span><span>Recent Trends</span><span>News</span>
    <svg width="14" height="14" viewBox="0 0 14 14"><circle cx="6" cy="6" r="4.5" fill="none" stroke="#777" stroke-width="1.5"/><path d="M9.5 9.5 13 13" stroke="#777" stroke-width="1.5"/></svg>
  </nav>
  <a class="btn-contact">Contact Us</a>
</header>

<section class="hero" role="img" aria-label="Wind turbines silhouetted against a sunset sky over water">
  <div class="hero-title">Varolu Corp</div>
  <div class="hero-sub">Solar Power Equipments &amp; Latest Products</div>
  <a class="btn-start">Get Started</a>
  <div class="hero-arrow" style="left:0"><svg width="28" height="44"><path d="M17 16l-6 6 6 6" fill="none" stroke="#fff" stroke-width="2"/></svg></div>
  <div class="hero-arrow" style="left:1172px"><svg width="28" height="44"><path d="M11 16l6 6-6 6" fill="none" stroke="#fff" stroke-width="2"/></svg></div>
</section>
<svg class="abs" style="left:0;top:520px" width="1200" height="80" viewBox="0 0 1200 80">
  <path d="M0 0 L600 40 L1200 0 L1200 80 L0 80Z" fill="#f39c12"/>
  <path d="M0 22 L600 70 L1200 22 L1200 80 L0 80Z" fill="#fff"/>
  <path d="M592 44l8 8 8-8" fill="none" stroke="#fff" stroke-width="2.5"/>
</svg>

<section class="about">
  <h2 class="section-title" style="top:652px">About Us</h2>
  <p class="abs" style="left:230px;top:700px;width:740px;text-align:center">Lorem Ipsum is simply dummy text of the printing and typesetting industry. Lorem Ipsum has been the industry's standard dummy text ever since the 1500s, when an unknown printer took a galley of type and scrambled standard dummy text ever since the 1500s, when an unknown printer took.</p>
  <div class="photo" style="left:88px;top:800px;width:494px;height:260px;background:linear-gradient(180deg,#6a5fb0 0%,#d9c9f0 40%,#8aa0c8 70%,#3e5040 100%)" role="img" aria-label="Power transmission towers at sunrise with a bright sun"></div>
  <div class="abs" style="left:650px;top:814px;width:460px">
    <h3 class="sub-title">In Addition</h3>
    <p>Lorem Ipsum is simply dummy text of the printing and typesetting industry. Lorem Ipsum has been the industry's standard dummy text ever since <span class="more">[...]</span></p>
    <div style="width:48px;height:3px;background:var(--green);margin:26px 0 30px"></div>
    <h3 class="sub-title">Industry Insight</h3>
    <p>Lorem Ipsum is simply dummy text of the printing and typesetting industry. Lorem Ipsum has been the industry's standard dummy ever since printing and typesetting industry. Lorem Ipsum has been the industry's standard dummy <span class="more">[...]</span></p>
  </div>
</section>

<section class="services">
  <h2 class="abs" style="left:147px;top:66px;font-size:31px;font-weight:400;color:var(--white)">Our Services</h2>
  <p class="abs" style="left:147px;top:110px;width:470px;color:var(--white)">Lorem Ipsum is simply dummy text of the printing and typesetting industry. Lorem Ipsum has been the industry's standard dummy text ever since...</p>
  <div class="photo" style="left:160px;top:212px;width:410px;height:264px;background:linear-gradient(160deg,#4a6fc8,#2c4a9a 60%,#b8c0c8 100%);opacity:.9" role="img" aria-label="Tilted solar panel on a mounting post"></div>
  <div class="service-item" style="top:70px"><div class="service-icon"><svg width="24" height="24"><circle cx="12" cy="12" r="9" fill="none" stroke="#333" stroke-width="1.6"/><path d="M7.5 12l3 3 6-6" fill="none" stroke="#333" stroke-width="1.6"/></svg></div><div><h4>Advisory Services.</h4><p>Lorem Ipsum is simply dummy text of the printing...</p></div></div>
  <svg class="abs" style="left:662px;top:182px" width="40" height="10"><path d="M0 5h40M4 1 0 5l4 4" stroke="#f39c12" stroke-width="1.6" fill="none"/></svg>
  <div class="service-item" style="top:163px"><div class="service-icon active"><svg width="24" height="24"><text x="12" y="18" text-anchor="middle" font-family="Roboto,sans-serif" font-size="18" fill="#fff">$</text></svg></div><div><h4>Financing Options.</h4><p>Lorem Ipsum is simply dummy text of the printing...</p></div></div>
  <div class="service-item" style="top:255px"><div class="service-icon"><svg width="26" height="24"><path d="M3 18c0-3 3-4 5-3 0-5 9-6 11-1 3 0 4 2 4 4z" fill="none" stroke="#333" stroke-width="1.6"/></svg></div><div><h4>Procurement &amp; Construction.</h4><p>Lorem Ipsum is simply dummy text of the printing...</p></div></div>
  <div class="service-item" style="top:348px"><div class="service-icon"><svg width="24" height="24"><path d="M3 12 12 4l9 8M6 10v10h12V10" fill="none" stroke="#333" stroke-width="1.6"/></svg></div><div><h4>Design &amp; Engineering.</h4><p>Lorem Ipsum is simply dummy text of the printing...</p></div></div>
</section>

<section class="projects">
  <nav class="filters"><span class="on">All</span><span>Household</span><span>Organization</span><span>Research</span><span>School</span><span>Solar Panels</span></nav>
  <h2 class="abs" style="left:88px;top:1722px;font-size:31px;font-weight:400;color:var(--ink)">Our Projects</h2>
  <p class="abs" style="left:88px;top:1770px;width:390px">Lorem Ipsum is simply dummy text of the printing and typesetting industry. Lorem Ipsum has been...</p>
  <div class="photo" style="left:88px;top:1856px;width:256px;height:264px;background:linear-gradient(180deg,#8fa6d8 0%,#d8e0f0 40%,#3a5fa0 60%,#5a8a3a 100%)" role="img" aria-label="Solar panel rows on a green field under a blue sky"></div>
  <div class="photo" style="left:351px;top:1856px;width:256px;height:264px;background:linear-gradient(180deg,#b8d8ee 0%,#e8f2f8 45%,#a8b0b8 70%,#7f8890 100%)" role="img" aria-label="Wind turbines beyond a paved plaza"></div>
  <div class="photo" style="left:613px;top:1730px;width:497px;height:390px;background:linear-gradient(180deg,#7a8494 0%,#4a5260 40%,#3e4638 75%,#5a4a30 100%)" role="img" aria-label="Ground-mounted solar panel array in a field">
    <div class="abs" style="left:205px;top:146px;width:38px;height:38px;border-radius:50%;background:#fff"></div>
    <div class="abs" style="left:251px;top:146px;width:38px;height:38px;border-radius:50%;background:#fff"></div>
    <svg class="abs" style="left:214px;top:155px" width="20" height="20"><path d="M8 12l4-4M6 10l-2 2a3 3 0 004 4l2-2M14 10l2-2a3 3 0 00-4-4l-2 2" stroke="#333" stroke-width="1.5" fill="none"/></svg>
    <svg class="abs" style="left:260px;top:155px" width="20" height="20"><circle cx="9" cy="9" r="5" fill="none" stroke="#333" stroke-width="1.5"/><path d="M13 13l4 4" stroke="#333" stroke-width="1.5"/></svg>
    <div class="abs" style="left:0;top:196px;width:100%;text-align:center;font-size:22px;color:#fff">Solar Panel</div>
    <div class="abs" style="left:0;top:228px;width:100%;text-align:center;font-size:12.5px;color:#fff">Lorem Ipsum is simply dummy text of the printing</div>
    <div class="abs" style="left:449px;top:352px;width:48px;height:38px;background:var(--orange)"><svg width="48" height="38"><path d="M17 25c1-6 5-9 12-9v-4l6 6-6 6v-4c-5 0-9 1-12 5z" fill="#fff"/></svg></div>
  </div>
</section>

<section class="news">
  <h2 class="section-title" style="top:66px">Latest News</h2>
  <div class="photo" style="left:88px;top:151px;width:382px;height:217px;background:linear-gradient(180deg,#c8ccd0 0%,#e8eaec 50%,#4a5a6a 65%,#6a9a40 100%)" role="img" aria-label="Solar panel array on a grassy hill under a cloudy sky"></div>
  <div class="date" style="left:88px;top:390px;background:var(--green)">11<br>APR</div>
  <div class="news-title" style="left:148px;top:396px">Lorem Ipsum is Simly Dummy Text...</div>
  <div class="byline" style="left:148px;top:424px">BY : Alan Merik</div>
  <p class="abs" style="left:88px;top:458px;width:390px">Lorem Ipsum is simply dummy text of the printing and typesetting industry. Lorem Ipsum has been the <span class="more">[...]</span></p>

  <div class="photo" style="left:515px;top:151px;width:125px;height:127px;background:linear-gradient(135deg,#3a6ab0,#8ab0e0 60%,#e0e8f0)" role="img" aria-label="Wind turbine in front of solar panels"></div>
  <div class="news-title" style="left:657px;top:150px">Lorem Ipsum is Simly Dummy Text...</div>
  <div class="byline" style="left:657px;top:182px">BY : Alan Merik</div>
  <div class="date" style="left:1064px;top:151px;background:var(--orange)">13<br>APR</div>
  <div class="abs" style="left:657px;top:208px;width:453px;height:1px;background:#ddd"></div>
  <p class="abs" style="left:657px;top:222px;width:453px;font-size:12px;line-height:21px">Lorem Ipsum is simply dummy text of the printing and typesetting industry lorem Ipsum has been the industry's standard dummy ever since <span class="more">[...]</span></p>

  <div class="photo" style="left:515px;top:324px;width:125px;height:127px;background:linear-gradient(180deg,#9ac0e8,#d8e4f0 40%,#3a5a90 60%,#5a8a3a)" role="img" aria-label="Solar panels in a green landscape"></div>
  <div class="news-title" style="left:657px;top:323px">Lorem Ipsum is Simly Dummy Text...</div>
  <div class="byline" style="left:657px;top:355px">BY : Alan Merik</div>
  <div class="date" style="left:1064px;top:324px;background:var(--orange)">13<br>APR</div>
  <div class="abs" style="left:657px;top:381px;width:453px;height:1px;background:#ddd"></div>
  <p class="abs" style="left:657px;top:395px;width:453px;font-size:12px;line-height:21px">Lorem Ipsum is simply dummy text of the printing and typesetting industry lorem Ipsum has been the industry's standard dummy ever since <span class="more">[...]</span></p>
</section>

<footer class="site-footer">
  <div class="brand f-brand" style="top:30px"><span class="brand-dot"></span>Varolu Corp.</div>
  <div class="contact-circle" style="left:265px;top:28px"><svg width="18" height="22"><path d="M9 21s-7-8-7-13a7 7 0 0114 0c0 5-7 13-7 13z" fill="#f39c12"/><circle cx="9" cy="8" r="2.5" fill="#333"/></svg></div>
  <p class="abs" style="left:322px;top:30px;width:240px;font-size:12px;line-height:20px">Some address line goes here, city name country name</p>
  <div class="abs" style="left:620px;top:20px;width:1px;height:66px;background:#3a3a3a"></div>
  <div class="contact-circle" style="left:650px;top:28px"><svg width="20" height="20"><path d="M4 2l4 1 1 4-2 2a11 11 0 005 5l2-2 4 1 0 4c-9 1-17-7-16-16z" fill="#f39c12"/></svg></div>
  <p class="abs" style="left:712px;top:42px;font-size:12px">+08 321 654 0987</p>
  <div class="abs" style="left:882px;top:20px;width:1px;height:66px;background:#3a3a3a"></div>
  <div class="contact-circle" style="left:935px;top:28px"><svg width="20" height="16"><rect x="1" y="1" width="18" height="14" fill="#f39c12"/><path d="M1 1l9 8 9-8" stroke="#333" stroke-width="1.5" fill="none"/></svg></div>
  <p class="abs" style="left:998px;top:42px;font-size:12px">www.varolucorp.com</p>
  <div class="abs" style="left:0;top:118px;width:1200px;height:1px;background:#333"></div>

  <div class="f-col" style="left:88px"><h5>Quick Links</h5><ul><li>Home</li><li>About Us</li><li>Services</li><li>Projects</li><li>Recent Trends</li><li>Solar Energy</li><li>News</li></ul></div>
  <div class="f-col" style="left:314px"><h5>Customer Care</h5><ul><li>Customer Service</li><li>Warranty Policy</li><li>Installation and Use</li><li>Contact Us</li><li>FAQ's</li><li>Privacy Policy</li><li>Terms &amp; Condition</li></ul></div>
  <div class="f-col social" style="left:602px"><h5>Follow Us</h5><ul><li><span class="dot"></span>Chatterly</li><li><span class="dot"></span>Birdline</li><li><span class="dot"></span>Searchly</li><li><span class="dot"></span>Linkwork</li><li><span class="dot"></span>Snapgram</li></ul></div>
  <div class="f-col" style="left:823px"><h5>Most Recent Trends</h5>
    <div style="width:287px;height:186px;background:linear-gradient(180deg,#8ab05a 0%,#e8e0d0 35%,#b84a3a 70%,#e8e8e8 100%)" role="img" aria-label="House with rooftop solar panels surrounded by trees"></div>
    <svg style="margin:10px 0 0 128px" width="30" height="8"><circle cx="4" cy="4" r="3" fill="#888"/><circle cx="15" cy="4" r="3" fill="#f39c12"/><circle cx="26" cy="4" r="3" fill="#888"/></svg>
  </div>
  <div class="copyright">Copy Right 2017. All Rights Reserved</div>
</footer>
<div class="to-top"><svg width="14" height="10"><path d="M2 8l5-5 5 5" fill="none" stroke="#333" stroke-width="2"/></svg></div>

</body>
</html>
```